Killer business card for bowling event and marketing company

Rapid 'Q' Promotions is a sports marketing company that specializes in unique bowling events that provide return on investment for sponsors and memorable experiences for participants and spectators. We need a new business card that simultaneously communicates professionalism and fun. Our preferred colors are black and re

Target Market(s)

Executives in the marketing and sponsorship departments of companies, tourism executives, bowling center owners, and people who love to bowl.

Industry/Entity Type

Business

Contact Information for Business Card

Dean T Walsh
Rapid 'Q' Promotions
PO Box 47
Ashford, Vermont USA 22871
Email: deant@rapidqpromotions.com
Mobile: 1-434-518-3762

Requirements
Must have
• Our preferred colors are black and red.
Nice to have
• I am considering the use of the attached image for the back of the card.

```html
<!DOCTYPE html>
<html lang="en">
<head>
<meta charset="utf-8">
<title>Rapid 'Q' Promotions – Business Card</title>
<link rel="stylesheet" href="https://fonts.googleapis.com/css2?family=Maven+Pro:wght@400;500;700&display=swap">
<style>
  :root {
    --stage: #c7c7c7;
    --card-light: #fbfbfb;
    --card-dark: #1b1b1b;
    --brand-red: #e8141b;
    --ink: #1f1f1f;
    --pin-light: #f3f3f3;
    --pin-mid: #dadada;
  }
  * { margin: 0; padding: 0; box-sizing: border-box; }
  html, body { width: 1200px; height: 900px; overflow: hidden; }
  body {
    background: var(--stage);
    font-family: "Maven Pro", sans-serif;
    position: relative;
  }
  .card {
    position: absolute;
    top: 271px;
    width: 457px;
    height: 281px;
    border-radius: 14px;
    overflow: hidden;
    box-shadow: 2px 3px 4px rgba(0, 0, 0, 0.25);
  }
  .card--front { left: 137px; background: var(--card-light); }
  .card--back { left: 626px; background: var(--card-dark); }

  .brand-name {
    position: absolute;
    font-weight: 700;
    line-height: 1;
    text-align: center;
    color: var(--brand-red);
  }
  .brand-name__main { display: block; font-size: 42px; letter-spacing: -0.5px; }
  .brand-name__sub { display: block; font-size: 19px; letter-spacing: 3px; margin-top: 4px; text-transform: uppercase; }
  .card--front .brand-name { left: 32px; top: 106px; width: 190px; }
  .card--back .brand-name { left: 0; right: 0; top: 102px; }
  .card--back .brand-name__main { font-size: 54px; }
  .card--back .brand-name__sub { font-size: 24px; letter-spacing: 4px; margin-top: 5px; }

  .divider {
    position: absolute;
    left: 235px;
    top: 89px;
    width: 1px;
    height: 104px;
    background: var(--brand-red);
  }
  .contact { position: absolute; left: 251px; top: 86px; color: var(--ink); }
  .contact__name {
    font-size: 21px;
    font-weight: 500;
    color: var(--brand-red);
    letter-spacing: 0.3px;
    text-transform: uppercase;
    white-space: nowrap;
  }
  .contact__name .initial { color: var(--ink); }
  .contact__phone {
    display: flex;
    align-items: center;
    gap: 7px;
    font-size: 14px;
    margin-top: 4px;
    margin-left: 1px;
  }
  .contact__address {
    font-size: 13px;
    line-height: 17px;
    font-style: normal;
    margin-top: 16px;
  }
  .pin-art {
    position: absolute;
    right: 0;
    top: 0;
    width: 60px;
    height: 100%;
    background: linear-gradient(90deg, var(--pin-light), var(--pin-mid));
    border-radius: 60px 0 0 30px;
    opacity: 0.8;
  }
</style>
</head>
<body>
  <section class="card card--front" aria-label="Card front">
    <div class="pin-art" role="img" aria-label="Bowling pin silhouette along the right edge"></div>
    <p class="brand-name">
      <span class="brand-name__main">Rapid 'Q'</span>
      <span class="brand-name__sub">Promotions</span>
    </p>
    <div class="divider"></div>
    <div class="contact">
      <p class="contact__name">Dean <span class="initial">T</span> Walsh</p>
      <p class="contact__phone">
        <svg width="7" height="12" viewBox="0 0 7 12" aria-hidden="true">
          <rect x="0.8" y="0.8" width="5.4" height="10.4" rx="1.2" fill="none" stroke="var(--brand-red)" stroke-width="1.6"/>
          <rect x="2.3" y="8.6" width="2.4" height="1.2" fill="var(--brand-red)"/>
        </svg>
        1-434-518-3762
      </p>
      <address class="contact__address">
        PO Box 47<br>
        Ashford,<br>
        Vermont USA 22871
      </address>
    </div>
  </section>

  <section class="card card--back" aria-label="Card back">
    <p class="brand-name">
      <span class="brand-name__main">Rapid 'Q'</span>
      <span class="brand-name__sub">Promotions</span>
    </p>
  </section>
</body>
</html>
```